Corvel Lease Homes
will not have subtitle
Corvel Lease Homes -
Creative Brief
Simple
Paul Venner, Tessa Venner
PO Box 58211 20415 #7 Rd Alderbrook, BC V2T 5K9
info@corvelholdings.ca
www.corvelholdings.ca
On front- white background with small logo and our contact info. Paul's # is 604.555.0187, mine is the other. would like all the colors to be the same as logo and info in blue. Back- blue background with large logo. I would also be interested in simply seeing what you all come up with as you know what looks best-so feel free to do something different than what I said and we'll go from there. Thank you.

```html
<!DOCTYPE html>
<html lang="en">
<head>
<meta charset="utf-8">
<title>Corvel Lease Homes – Business Cards</title>
<link href="https://fonts.googleapis.com/css2?family=Cinzel:wght@600;700&family=Open+Sans:wght@400;600&display=swap" rel="stylesheet">
<style>
  :root {
    --stage: #eceef1;
    --card-white: #ffffff;
    --card-shade: #e6e8eb;
    --brand-blue: #1f5f9a;
    --brand-deep: #0f3e6e;
    --brand-light: #3a8bc9;
    --text-grey: #4a5560;
    --rule-grey: #c9ced4;
  }
  * { margin: 0; padding: 0; box-sizing: border-box; }
  html, body { width: 1200px; height: 876px; overflow: hidden; }
  body {
    background: var(--stage);
    font-family: "Open Sans", Arial, sans-serif;
    position: relative;
  }
  .card {
    position: absolute;
    width: 520px;
    height: 300px;
    border-radius: 12px;
    overflow: hidden;
    box-shadow: 0 6px 18px rgba(0,0,0,0.18);
  }
  /* Front */
  .card-front {
    left: 50px; top: 90px;
    background: linear-gradient(180deg, var(--card-white) 0%, var(--card-white) 60%, var(--card-shade) 100%);
  }
  .front-brand {
    position: absolute;
    left: 30px; top: 98px;
    width: 220px;
    font-family: "Cinzel", Georgia, serif;
    font-weight: 700;
    font-size: 30px;
    line-height: 1.1;
    color: var(--brand-blue);
  }
  .front-divider {
    position: absolute;
    left: 262px; top: 50px;
    width: 1px; height: 170px;
    background: var(--rule-grey);
  }
  .front-contacts {
    position: absolute;
    left: 282px; top: 50px;
    width: 220px;
    color: var(--text-grey);
    font-size: 10px;
    line-height: 1.45;
  }
  .contact-name {
    font-family: "Cinzel", Georgia, serif;
    font-weight: 600;
    font-size: 18px;
    color: var(--brand-blue);
    line-height: 1.15;
  }
  .contact-person { margin-bottom: 12px; }
  .contact-details { margin-top: 4px; }
  .front-band {
    position: absolute;
    left: 0; bottom: 0;
    width: 100%; height: 30px;
    background: linear-gradient(90deg, var(--brand-deep), var(--brand-light));
    color: #fff;
    font-size: 10px;
    letter-spacing: 2px;
    text-transform: uppercase;
    display: flex; align-items: center; justify-content: center;
  }
  /* Blue back */
  .card-back-blue {
    left: 630px; top: 90px;
    background: radial-gradient(circle at 60% 35%, var(--brand-light) 0%, var(--brand-blue) 45%, var(--brand-deep) 100%);
    color: #fff;
  }
  /* White back */
  .card-back-white {
    left: 340px; top: 500px;
    background: linear-gradient(180deg, var(--card-white) 0%, var(--card-white) 55%, var(--card-shade) 100%);
    color: var(--brand-blue);
  }
  .back-layout {
    position: absolute; inset: 0;
    display: flex; flex-direction: column;
    align-items: center; justify-content: center;
    gap: 28px;
  }
  .back-brand {
    font-family: "Cinzel", Georgia, serif;
    font-weight: 700;
    font-size: 36px;
  }
  .back-web {
    font-family: "Cinzel", Georgia, serif;
    font-weight: 700;
    font-size: 17px;
    letter-spacing: 0.5px;
  }
</style>
</head>
<body>

  <section class="card card-front" aria-label="Card front">
    <div class="front-brand">Corvel Lease Homes</div>
    <div class="front-divider"></div>
    <div class="front-contacts">
      <div class="contact-person">
        <div class="contact-name">Tessa Venner</div>
        <div>Phone: 604.555.0142</div>
      </div>
      <div class="contact-person">
        <div class="contact-name">Paul Venner</div>
        <div>Phone: 604.555.0187</div>
      </div>
      <div class="contact-details">
        <div>PO Box 58211 20415 #7 Rd</div>
        <div>Alderbrook, BC V2T 5K9</div>
        <div>Fax: 604.555.0199</div>
        <div>Email: info@corvelholdings.ca</div>
      </div>
    </div>
    <div class="front-band">www.corvelholdings.ca</div>
  </section>

  <section class="card card-back-blue" aria-label="Card back, blue">
    <div class="back-layout">
      <div class="back-brand">Corvel Lease Homes</div>
      <div class="back-web">www.corvelholdings.ca</div>
    </div>
  </section>

  <section class="card card-back-white" aria-label="Card back, white">
    <div class="back-layout">
      <div class="back-brand">Corvel Lease Homes</div>
      <div class="back-web">www.corvelholdings.ca</div>
    </div>
  </section>

</body>
</html>
```